Stationery Design Project for Bramble Co

Hi All,

We need you to design stationary for a new online financial services business. We have already got the logo designed and it is attached. If you would like it in any other formats please let me know. If you could also if possible, match the fonts in your design to that on the logo’s provided.

What we need:
- Business Card
- A4 Letter head
- A4 Folders
- PPT template (Title page and regular page)

And what ever else you want to throw in.

We are in the process of getting the web site designed, however below is a list of websites which we like which will give you an understanding of the style that we are going for.

- plimo.com
- brambleroute.com
- tallowquay.com
- pelkwintry.com

I look forward to your seeing your design.

Industry/Entity Type

Financial

Requirements
Must have
• Outputs:
- Documents ready to print
- Generic editable information
- Pdf copies of the documents
- Word version of letterhead

```html
<!DOCTYPE html>
<html lang="en">
<head>
<meta charset="utf-8">
<title>Bramble Co Stationery</title>
<link href="https://fonts.googleapis.com/css2?family=Questrial&display=swap" rel="stylesheet">
<style>
  :root {
    --navy: #10304a;
    --orange: #f7941d;
    --blue: #0a7fa8;
    --grey-text: #555a60;
    --paper: #ffffff;
    --backdrop: #dcdcd8;
    --watermark: #fdf2e8;
  }
  * { margin: 0; padding: 0; box-sizing: border-box; }
  html, body {
    width: 1200px; height: 849px; overflow: hidden;
    background: var(--backdrop);
    font-family: "Questrial", "Century Gothic", sans-serif;
  }
  .canvas { position: relative; width: 1200px; height: 849px; }

  .letterhead {
    position: absolute; left: 67px; top: 26px; width: 616px; height: 798px;
    background: var(--paper);
    border-bottom: 9px solid var(--blue);
  }
  .brand { position: absolute; display: flex; align-items: center; white-space: nowrap; }
  .brand-dot { border-radius: 50%; background: var(--orange); flex: none; }
  .brand-name { color: var(--navy); line-height: 1; }

  .letterhead .brand { left: 318px; top: 40px; }
  .letterhead .brand-dot { width: 46px; height: 46px; margin-right: 16px; }
  .letterhead .brand-name { font-size: 31px; }

  .letterhead-watermark {
    position: absolute; left: 170px; top: 260px; width: 276px; height: 276px;
    border-radius: 50%; background: var(--watermark);
  }

  .letterhead-footer {
    position: absolute; left: 39px; right: 40px; top: 755px;
    display: flex; justify-content: space-between;
    font-size: 9px; line-height: 11px; color: var(--grey-text);
  }
  .label { color: var(--orange); }

  .card {
    position: absolute; width: 253px; height: 147px;
  }
  .card-front {
    left: 585px; top: 171px; background: var(--paper);
    border-bottom: 5px solid var(--blue);
  }
  .card-front .brand { left: 17px; top: 44px; flex-direction: column; align-items: center; }
  .card-front .brand-dot { width: 42px; height: 42px; margin-bottom: 8px; }
  .card-front .brand-name { font-size: 21px; }
  .card-details {
    position: absolute; left: 153px; top: 36px;
    font-size: 7.5px; line-height: 8.4px; color: var(--grey-text);
  }
  .card-person { font-size: 11px; line-height: 12px; color: var(--navy); }
  .card-role { color: var(--orange); margin-bottom: 6px; }

  .card-back { left: 882px; top: 172px; height: 145px; background: var(--blue); }
  .card-back .brand { left: 25px; top: 55px; }
  .card-back .brand-dot { width: 36px; height: 36px; margin-right: 12px; }
  .card-back .brand-name { font-size: 21px; color: #ffffff; }
</style>
</head>
<body>
<main class="canvas">
  <section class="letterhead" aria-label="A4 letterhead">
    <div class="brand">
      <span class="brand-dot"></span>
      <span class="brand-name">brambleco.com</span>
    </div>
    <div class="letterhead-watermark" aria-hidden="true"></div>
    <footer class="letterhead-footer">
      <div>BRAMBLE CO PTY LTD<br>&nbsp;ABN&nbsp; 12345678901</div>
      <div>27 Harlow Lane<br>Sydney&nbsp; NSW&nbsp; 2000</div>
      <div><span class="label">Phone</span> : (02)&nbsp; 9999&nbsp; 9999<br><span class="label">Fax</span>&nbsp;&nbsp;&nbsp;&nbsp;&nbsp; : (02)&nbsp; 9999&nbsp; 9999</div>
      <div>info@brambleco.com<br>www.brambleco.com</div>
    </footer>
  </section>

  <section class="card card-front" aria-label="Business card front">
    <div class="brand">
      <span class="brand-dot"></span>
      <span class="brand-name">Bramble Co</span>
    </div>
    <div class="card-details">
      <div class="card-person">John Doe</div>
      <div class="card-role">Director</div>
      <div>27 Harlow Lane</div>
      <div>Sydney&nbsp; NSW&nbsp; 2000</div>
      <div><span class="label">Phone</span> : (02) 9999 9999</div>
      <div><span class="label">Fax</span>&nbsp;&nbsp;&nbsp;&nbsp; : (02) 9999 9999</div>
      <div>info@brambleco.com</div>
      <div>www.brambleco.com</div>
    </div>
  </section>

  <section class="card card-back" aria-label="Business card back">
    <div class="brand">
      <span class="brand-dot"></span>
      <span class="brand-name">brambleco.com</span>
    </div>
  </section>
</main>
</body>
</html>
```